Brisko Sky Park needs a new upscale business card design for our high end aircraft hangar complex

Brisko Sky Park (BSP) is a large, upscale jet hangar complex in the US housing expensive aircraft. We need a new business card design, using our current logo. We will be attending a industry convention and need a card design that will stand out and be remembered by aircraft owners and private pilots.

Target Market(s)

Aircraft pilots or owners looking for a new upscale hangar

Industry/Entity Type

Airport

Contact Information for Business Card

I like to use very heavy card stock, 400#, double sided. Square, no rounded edges please.

Colors
3276b5
0255a3
85abd2

Requirements
Must have
• An expensive, classy design, vivid colors.
Nice to have
• Needs to look very expensive and classy, and have some "pop". Designer must be able to download or copy my current typeface or fonts.
• One card side might be black with the "Logo and Brisko Sky Park Double line image in blue (or try gold, or glossy black), and perhaps have a grayed out "K480 jet silhouette". The other card side would have our contact info, and perhaps the "BSP Logo only". I'd like my contact info 'stacked', not in a paragraph format.
Should not have
• Should not look "too busy". Having a double-sided card will help.

```html
<!DOCTYPE html>
<html lang="en">
<head>
<meta charset="utf-8">
<title>Brisko Sky Park – Business Card</title>
<link rel="stylesheet" href="https://fonts.googleapis.com/css2?family=Saira:wght@600&family=PT+Sans:wght@400&display=swap">
<style>
  :root {
    --backdrop: #8c8d8f;
    --card: #121213;
    --card-edge: #1b1b1c;
    --brand-blue: #3276b5;
    --brand-deep: #0255a3;
    --brand-light: #85abd2;
    --text-light: #e4e4e4;
    --rule: #8a8a8a;
    --strip-grey: #b9babc;
  }
  * { margin: 0; padding: 0; box-sizing: border-box; }
  html, body {
    width: 1105px; height: 1200px; overflow: hidden;
    background: var(--backdrop);
  }
  .canvas { position: relative; width: 1105px; height: 1200px; }
  .card {
    position: absolute; left: 182px; width: 746px; height: 424px;
    background: var(--card);
    box-shadow: 0 10px 22px rgba(0,0,0,.35);
    overflow: hidden;
  }
  .card-front { top: 119px; }
  .card-back { top: 637px; }

  .wordmark {
    position: absolute;
    font-family: 'Saira', sans-serif; font-weight: 600;
    color: var(--brand-blue);
    line-height: 1;
  }
  .front-wordmark { right: 42px; top: 50px; font-size: 92px; letter-spacing: 4px; }

  .holder-name {
    position: absolute; left: 39px; top: 166px;
    font-family: 'Saira', sans-serif; font-weight: 600;
    font-size: 27px; letter-spacing: .5px; color: var(--brand-blue);
  }
  .holder-title {
    position: absolute; left: 39px; top: 199px;
    font-family: 'PT Sans', sans-serif; font-size: 19px; color: var(--text-light);
  }
  .divider {
    position: absolute; left: 39px; top: 240px; width: 666px; height: 1px;
    background: var(--rule);
  }
  .contact-list {
    position: absolute; left: 39px; top: 256px; list-style: none;
    font-family: 'PT Sans', sans-serif; font-size: 19px; line-height: 28.5px;
    color: var(--text-light);
  }
  .contact-list .label { color: var(--brand-blue); display: inline-block; width: 20px; }
  .address {
    position: absolute; right: 41px; top: 309px; text-align: right;
    font-family: 'PT Sans', sans-serif; font-size: 19px; line-height: 28px;
    color: var(--text-light);
  }
  .front-band { position: absolute; left: 0; bottom: 0; }
  .website {
    position: absolute; left: 458px; top: 394px; width: 260px; text-align: center;
    font-family: 'PT Sans', sans-serif; font-size: 18px; letter-spacing: 4px;
    color: var(--text-light);
  }

  .jet-silhouette {
    position: absolute; left: 356px; top: 0; width: 390px; height: 424px;
    background: radial-gradient(ellipse at 60% 62%, #2a2a2c 0%, #1c1c1e 40%, rgba(18,18,19,0) 75%);
  }
  .back-logo { position: absolute; left: 76px; top: 95px; }
  .back-wordmark { position: static; font-size: 132px; letter-spacing: 6px; }
  .back-name {
    font-family: 'Saira', sans-serif; font-weight: 600;
    font-size: 34px; line-height: 1.1; color: var(--brand-blue);
    text-transform: uppercase; letter-spacing: 1px; margin-top: 6px;
  }
</style>
</head>
<body>
<div class="canvas">

  <section class="card card-front">
    <div class="wordmark front-wordmark">BSP</div>

    <h1 class="holder-name">DANIEL REYES</h1>
    <p class="holder-title">CEO/Founder</p>
    <div class="divider"></div>

    <ul class="contact-list">
      <li><span class="label">P</span>(555) 214-7730</li>
      <li><span class="label">C</span>(555) 381-0462</li>
      <li><span class="label">F</span>(555) 907-5518</li>
      <li><span class="label">E</span>hello@briskosky.com</li>
    </ul>

    <address class="address" style="font-style:normal">
      1420 Hangar Row<br>Tulsa, Oklahoma 74115
    </address>

    <svg class="front-band" width="746" height="36" viewBox="0 0 746 36" aria-hidden="true">
      <path d="M0 10 H428 Q438 10 430 16 L420 24 H0 Z" fill="var(--strip-grey)"/>
      <path d="M0 24 H420 L430 16 Q440 5 458 4 H746 V36 H0 Z" fill="var(--brand-deep)"/>
      <path d="M446 36 Q450 6 478 4 H746 V36 Z" fill="var(--brand-blue)"/>
    </svg>
    <div class="website">www.briskosky.com</div>
  </section>

  <section class="card card-back">
    <div class="jet-silhouette" role="img" aria-label="Faint greyed-out K480 business jet seen from the front"></div>
    <div class="back-logo">
      <div class="wordmark back-wordmark">BSP</div>
      <div class="back-name">Brisko Sky Park</div>
    </div>
  </section>

</div>
</body>
</html>
```